Brightpath Consulting WA Business Card

Create an interesting, eye catching and colourful two sided business card. We are a business consulting operation assisting SME's improve all areas of their business. We provide consulting services to assist SME's to create a culture of continuous improvement, making a positive difference in the business. Our tag line is Small changes, big rewards. We want to create a well recognised, innovative brand that can be continued throughout our website, social media and email correspondence.

Target Market(s)

Small to Medium Enterprise Business Owners

Industry/Entity Type

Business Consultant

Contact Information for Business Card

Name of Business: Brightpath Consulting - Small Changes Big Rewards
Dean Morrow Ph 0407358164 Lydia Morrow Ph 0409583417
Email brightpathconsultingwa@examplemail.com
Web address TBA
FaceBook page TBA

BACKSIDE OF CARD

Providing assistance with:

• Organisation & Efficiency
• Revenue generation & Marketing
• Financial Management
• Production quality & delivery
• Systems & Process documentation
• Exit Strategy

Font styles to use
Other font styles liked:
• Calibri

Colors

Designer to choose colors to be used in the design.

Requirements
Must have
• Calibri font

```html
<!DOCTYPE html>
<html lang="en">
<head>
<meta charset="utf-8">
<title>Brightpath Consulting WA Business Card</title>
<link href="https://fonts.googleapis.com/css2?family=Carlito:ital,wght@0,400;0,700;1,400;1,700&display=swap" rel="stylesheet">
<style>
  :root {
    --bg: #2b2b2d;
    --card: #ffffff;
    --blue: #1b73b8;
    --sky: #4fb3dd;
    --red: #e8412c;
    --orange: #f28c1e;
    --yellow: #f6d23a;
    --green: #8cc63f;
    --ink: #3a3a3a;
    --white: #ffffff;
  }
  * { box-sizing: border-box; margin: 0; padding: 0; }
  html, body { width: 1200px; height: 903px; overflow: hidden; }
  body {
    background: var(--bg);
    font-family: "Carlito", "Calibri", sans-serif;
    position: relative;
  }
  .card {
    position: absolute;
    left: 290px;
    width: 620px;
    height: 354px;
    border-radius: 22px;
    background: var(--card);
    overflow: hidden;
  }
  .card-back { top: 62px; }
  .card-front { top: 487px; }

  /* back side */
  .brand-strip {
    position: absolute; left: 0; top: 0; width: 138px; height: 100%;
    display: flex; align-items: center; justify-content: center;
  }
  .brand-strip .brand-stack {
    transform: rotate(90deg);
    white-space: nowrap;
    text-align: left;
  }
  .brand-name {
    color: var(--blue); font-weight: 700; text-transform: uppercase;
    letter-spacing: 1px; white-space: nowrap;
  }
  .brand-strip .brand-name { font-size: 27px; }
  .tagline { font-style: italic; font-weight: 700; color: var(--red); white-space: nowrap; }
  .brand-strip .tagline { font-size: 21px; }
  .service-panel {
    position: absolute; left: 138px; top: 0; right: 0; bottom: 0;
    background: linear-gradient(30deg, var(--blue) 0%, #3a6fb2 22%, var(--red) 52%, var(--orange) 66%, var(--green) 84%, var(--yellow) 100%);
    color: var(--white);
    padding: 52px 40px 0 44px;
    text-transform: uppercase;
  }
  .service-heading { font-size: 21px; font-weight: 700; letter-spacing: .5px; margin-bottom: 22px; }
  .service-list { list-style: none; }
  .service-list li {
    font-size: 19px; font-weight: 700; letter-spacing: .4px;
    display: flex; align-items: center; gap: 14px; margin-bottom: 11px;
  }
  .service-list li::before {
    content: ""; width: 14px; height: 14px; background: var(--white); flex: none;
  }

  /* front side */
  .decor-art {
    position: absolute; right: 0; top: 0; width: 190px; height: 210px;
    border-bottom-left-radius: 120px;
    background: linear-gradient(135deg, var(--sky) 0%, var(--red) 35%, var(--yellow) 62%, var(--green) 100%);
    opacity: .9;
  }
  .front-brand { position: absolute; left: 36px; top: 34px; }
  .front-brand .brand-name { font-size: 32px; }
  .front-brand .tagline { font-size: 20px; margin-top: -2px; }
  .contacts { position: absolute; left: 36px; top: 146px; }
  .people { display: flex; gap: 40px; margin-bottom: 10px; }
  .person-name { font-size: 25px; font-weight: 700; color: var(--ink); text-transform: uppercase; letter-spacing: .5px; line-height: 30px; }
  .line { display: flex; align-items: center; gap: 9px; font-size: 22px; line-height: 27px; white-space: nowrap; }
  .person .line { color: var(--blue); }
  .icon { width: 22px; height: 22px; flex: none; }
  .details .line { color: var(--ink); margin-top: 5px; }
  .social-bar {
    position: absolute; left: 0; right: 0; top: 290px; height: 26px;
  }
  .social-rule { position: absolute; left: 36px; right: 200px; top: 20px; height: 4px; background: var(--green); }
  .social-tab {
    position: absolute; right: 0; top: 0; height: 26px; width: 200px;
    background: var(--sky); color: var(--white);
    display: flex; align-items: center; gap: 8px; padding-left: 16px; font-size: 17px;
    clip-path: polygon(12px 0, 100% 0, 100% 100%, 0 100%);
  }
  .social-tab .dot { width: 13px; height: 13px; background: var(--white); }
  .base-rule { position: absolute; left: 36px; right: 36px; bottom: 20px; height: 7px; background: var(--green); }
</style>
</head>
<body>

<section class="card card-back" aria-label="Business card back">
  <div class="brand-strip">
    <div class="brand-stack">
      <div class="brand-name">Brightpath Consulting</div>
      <div class="tagline">Small Changes Big Rewards</div>
    </div>
  </div>
  <div class="service-panel">
    <h2 class="service-heading">Creating a culture of continuous improvement</h2>
    <ul class="service-list">
      <li>Organisation &amp; Efficiency</li>
      <li>Revenue Generation &amp; Marketing</li>
      <li>Financial Management</li>
      <li>Production Quality &amp; Delivery</li>
      <li>Systems &amp; Process Documentation</li>
      <li>Exit Strategy</li>
    </ul>
  </div>
</section>

<section class="card card-front" aria-label="Business card front">
  <div class="decor-art" role="img" aria-label="Colourful abstract decoration in blue, red, yellow and green"></div>
  <div class="front-brand">
    <div class="brand-name">Brightpath Consulting</div>
    <div class="tagline">Small Changes Big Rewards</div>
  </div>
  <div class="contacts">
    <div class="people">
      <div class="person">
        <div class="person-name">Dean Morrow</div>
        <div class="line">
          <svg class="icon" viewBox="0 0 24 24"><rect width="24" height="24" rx="5" fill="#1b73b8"/><path d="M7 6c1-1 2 0 3 2s0 2-1 3c1 2 2 3 4 4 1-1 1-2 3-1s3 2 2 3c-1 2-4 2-7 0s-5-5-5-8c0-1 0-2 1-3z" fill="#fff"/></svg>
          0407358164
        </div>
      </div>
      <div class="person">
        <div class="person-name">Lydia Morrow</div>
        <div class="line">
          <svg class="icon" viewBox="0 0 24 24"><rect width="24" height="24" rx="5" fill="#1b73b8"/><path d="M7 6c1-1 2 0 3 2s0 2-1 3c1 2 2 3 4 4 1-1 1-2 3-1s3 2 2 3c-1 2-4 2-7 0s-5-5-5-8c0-1 0-2 1-3z" fill="#fff"/></svg>
          0409583417
        </div>
      </div>
    </div>
    <div class="details">
      <div class="line">
        <svg class="icon" viewBox="0 0 24 24"><rect width="24" height="24" rx="5" fill="#e8412c"/><rect x="5" y="7" width="14" height="10" fill="none" stroke="#fff" stroke-width="1.6"/><path d="M5 7l7 6 7-6" fill="none" stroke="#fff" stroke-width="1.6"/></svg>
        brightpathconsultingwa@examplemail.com
      </div>
      <div class="line">
        <svg class="icon" viewBox="0 0 24 24"><rect width="24" height="24" rx="5" fill="#f28c1e"/><circle cx="12" cy="12" r="6.5" fill="none" stroke="#fff" stroke-width="1.5"/><path d="M5.5 12h13M12 5.5c-3 3.5-3 9.5 0 13M12 5.5c3 3.5 3 9.5 0 13" fill="none" stroke="#fff" stroke-width="1.3"/></svg>
        brightpathconsultingwa.example
      </div>
    </div>
  </div>
  <div class="social-bar">
    <div class="social-rule"></div>
    <div class="social-tab"><span>brightpathconsulting</span><span class="dot"></span></div>
  </div>
  <div class="base-rule"></div>
</section>

</body>
</html>
```